MORVETH ELECTRICAL CONTRACTING - Electrical business

I need a design to go over a new van.
It needs to include;
The logo (All over, you decide)
phone number - 0417362850 (large)
email - kieran@morvethelectrical.example (medium)
website - www.morvethelectrical.example (small)
EC number - EC58216 (small)
"DOMESTIC & COMMERCIAL" (medium)
The facebook and instagram logos

I have uploaded the new van
my 2 logos
my existing ute as an idea
and a friends ute as another idea (sharp)

```html
<!DOCTYPE html>
<html lang="en">
<head>
<meta charset="utf-8">
<title>Morveth Electrical Contracting – Van Wrap</title>
<link rel="stylesheet" href="https://fonts.googleapis.com/css2?family=Montserrat:wght@500&family=Open+Sans+Condensed:wght@300;700&family=Open+Sans:wght@400;600&display=swap">
<style>
  :root {
    --stage: #e6e7e9;
    --wrap-white: #f7f7f6;
    --wrap-black: #050505;
    --brand-red: #d8191f;
    --brand-blue: #2c35b5;
    --phone-violet: #5b3fc0;
    --link-blue: #4a63d8;
    --muted: #6c6c70;
    --glow-deep: #170c4a;
    --glow-bright: #6a48ff;
  }
  html, body {
    margin: 0;
    padding: 0;
    width: 1200px;
    height: 2656px;
    overflow: hidden;
    background: var(--stage);
  }
  .sheet {
    position: relative;
    width: 1200px;
    height: 2656px;
  }
  .wrap-panel {
    position: absolute;
    left: 50px;
    display: block;
    filter: drop-shadow(0 10px 18px rgba(0,0,0,0.18));
  }
  .wrap-panel--driver { top: 180px; }
  .wrap-panel--rear { top: 900px; left: 270px; }
  .wrap-panel--passenger { top: 1840px; }
  .wordmark {
    font-family: "Montserrat", sans-serif;
    font-weight: 500;
    fill: var(--brand-red);
  }
  .service-line {
    font-family: "Open Sans Condensed", "Open Sans", sans-serif;
    font-weight: 700;
    fill: var(--brand-blue);
  }
  .phone {
    font-family: "Open Sans Condensed", "Open Sans", sans-serif;
    font-weight: 700;
    fill: var(--phone-violet);
  }
  .contact {
    font-family: "Open Sans", sans-serif;
    font-weight: 400;
    fill: var(--link-blue);
  }
  .licence {
    font-family: "Open Sans", sans-serif;
    font-weight: 400;
    fill: var(--muted);
  }
  .social-dot { fill: var(--brand-red); }
  .panel-white { fill: var(--wrap-white); }
  .panel-black { fill: var(--wrap-black); }
  .panel-red { fill: var(--brand-red); }
</style>
</head>
<body>
<main class="sheet">

  <svg class="wrap-panel wrap-panel--driver" width="1100" height="500" viewBox="0 0 1100 500" aria-label="Driver side wrap">
    <defs>
      <radialGradient id="glowDriver" cx="0.55" cy="0.25" r="0.6">
        <stop offset="0" stop-color="var(--glow-bright)"/>
        <stop offset="0.45" stop-color="var(--glow-deep)"/>
        <stop offset="1" stop-color="var(--wrap-black)"/>
      </radialGradient>
      <clipPath id="clipDriver">
        <path d="M560,0 H1100 V500 H720 C700,420 640,380 620,300 C600,220 700,160 640,80 C610,40 560,30 560,0 Z"/>
      </clipPath>
    </defs>
    <rect class="panel-white" width="1100" height="500" rx="18"/>
    <path class="panel-red" transform="translate(-18,0)" d="M560,0 H1100 V500 H720 C700,420 640,380 620,300 C600,220 700,160 640,80 C610,40 560,30 560,0 Z"/>
    <path class="panel-black" d="M560,0 H1100 V500 H720 C700,420 640,380 620,300 C600,220 700,160 640,80 C610,40 560,30 560,0 Z"/>
    <rect clip-path="url(#clipDriver)" x="560" y="0" width="540" height="280" fill="url(#glowDriver)" role="img" aria-label="Photo of a hand touching a glowing purple electric arc"/>
    <circle class="social-dot" cx="640" cy="60" r="10"/>
    <circle class="social-dot" cx="668" cy="60" r="10"/>
    <text class="service-line" x="885" y="200" font-size="30" text-anchor="middle">DOMESTIC &amp; COMMERCIAL</text>
    <text class="phone" x="885" y="262" font-size="58" text-anchor="middle">0417362850</text>
    <text class="contact" x="885" y="300" font-size="18" text-anchor="middle">kieran@morvethelectrical.example</text>
    <text class="contact" x="885" y="324" font-size="15" text-anchor="middle">www.morvethelectrical.example</text>
    <text class="licence" x="1050" y="430" font-size="12" text-anchor="end">EC58216</text>
    <text class="wordmark" x="310" y="330" font-size="64" letter-spacing="14" text-anchor="middle">MORVETH</text>
    <text class="wordmark" x="310" y="372" font-size="20" letter-spacing="7" text-anchor="middle">ELECTRICAL CONTRACTING</text>
  </svg>

  <svg class="wrap-panel wrap-panel--rear" width="660" height="640" viewBox="0 0 660 640" aria-label="Rear door wrap">
    <defs>
      <radialGradient id="glowRear" cx="0.55" cy="0.1" r="0.7">
        <stop offset="0" stop-color="var(--glow-bright)"/>
        <stop offset="0.45" stop-color="var(--glow-deep)"/>
        <stop offset="1" stop-color="var(--wrap-black)"/>
      </radialGradient>
      <clipPath id="clipRear">
        <path d="M60,20 H640 V290 H230 C150,270 90,240 80,170 C70,110 100,60 60,20 Z"/>
      </clipPath>
    </defs>
    <rect class="panel-white" width="660" height="640" rx="26"/>
    <path class="panel-red" transform="translate(-14,6)" d="M60,20 H640 V290 H230 C150,270 90,240 80,170 C70,110 100,60 60,20 Z"/>
    <path class="panel-black" d="M60,20 H640 V290 H230 C150,270 90,240 80,170 C70,110 100,60 60,20 Z"/>
    <rect clip-path="url(#clipRear)" x="60" y="20" width="580" height="270" fill="url(#glowRear)" role="img" aria-label="Photo of a hand touching a glowing purple electric arc"/>
    <circle class="social-dot" cx="110" cy="70" r="10"/>
    <circle class="social-dot" cx="138" cy="70" r="10"/>
    <text class="service-line" x="390" y="80" font-size="28" text-anchor="middle">DOMESTIC &amp; COMMERCIAL</text>
    <text class="phone" x="390" y="138" font-size="54" text-anchor="middle">0417362850</text>
    <text class="contact" x="390" y="176" font-size="17" text-anchor="middle">kieran@morvethelectrical.example</text>
    <text class="contact" x="390" y="200" font-size="15" text-anchor="middle">www.morvethelectrical.example</text>
    <text class="licence" x="390" y="228" font-size="11" text-anchor="middle">EC58216</text>
    <text class="wordmark" x="330" y="470" font-size="60" letter-spacing="13" text-anchor="middle">MORVETH</text>
    <text class="wordmark" x="330" y="512" font-size="19" letter-spacing="6" text-anchor="middle">ELECTRICAL CONTRACTING</text>
  </svg>

  <svg class="wrap-panel wrap-panel--passenger" width="1100" height="500" viewBox="0 0 1100 500" aria-label="Passenger side wrap">
    <defs>
      <radialGradient id="glowPassenger" cx="0.45" cy="0.25" r="0.6">
        <stop offset="0" stop-color="var(--glow-bright)"/>
        <stop offset="0.45" stop-color="var(--glow-deep)"/>
        <stop offset="1" stop-color="var(--wrap-black)"/>
      </radialGradient>
      <clipPath id="clipPassenger">
        <path transform="translate(1100,0) scale(-1,1)" d="M560,0 H1100 V500 H720 C700,420 640,380 620,300 C600,220 700,160 640,80 C610,40 560,30 560,0 Z"/>
      </clipPath>
    </defs>
    <rect class="panel-white" width="1100" height="500" rx="18"/>
    <g transform="translate(1100,0) scale(-1,1)">
      <path class="panel-red" transform="translate(-18,0)" d="M560,0 H1100 V500 H720 C700,420 640,380 620,300 C600,220 700,160 640,80 C610,40 560,30 560,0 Z"/>
      <path class="panel-black" d="M560,0 H1100 V500 H720 C700,420 640,380 620,300 C600,220 700,160 640,80 C610,40 560,30 560,0 Z"/>
    </g>
    <rect clip-path="url(#clipPassenger)" x="0" y="0" width="540" height="280" fill="url(#glowPassenger)" role="img" aria-label="Photo of a hand touching a glowing purple electric arc"/>
    <circle class="social-dot" cx="432" cy="60" r="10"/>
    <circle class="social-dot" cx="460" cy="60" r="10"/>
    <text class="service-line" x="215" y="200" font-size="30" text-anchor="middle">DOMESTIC &amp; COMMERCIAL</text>
    <text class="phone" x="215" y="262" font-size="58" text-anchor="middle">0417362850</text>
    <text class="contact" x="215" y="300" font-size="18" text-anchor="middle">kieran@morvethelectrical.example</text>
    <text class="contact" x="215" y="324" font-size="15" text-anchor="middle">www.morvethelectrical.example</text>
    <text class="licence" x="50" y="430" font-size="12">EC58216</text>
    <text class="wordmark" x="790" y="330" font-size="64" letter-spacing="14" text-anchor="middle">MORVETH</text>
    <text class="wordmark" x="790" y="372" font-size="20" letter-spacing="7" text-anchor="middle">ELECTRICAL CONTRACTING</text>
  </svg>

</main>
</body>
</html>
```